Four nights by a quiet harbour

Creation of the cover for the book: "Trois saisons au bord du vieux port" with the joined photo of a 70 years old lady.
Title: "Four nights beside the quiet harbour"
Author: "Mireille Cantal"
Publisher: "Editions Basalte" (should be at the bottom of the page)
Format: 14 x 20.5 cm
The story: A senior lady (70 years old), divorced, with a beautiful face, still wants to seduce, even young men.
We found the perfect photo for the woman. We would like to ask you to make a modern cover from it.
Updates
Besoin de quelques jours pour choisir un design
Target Market(s)
Novels reader (adults)
Industry/Entity Type
book
Look and feel
Each slider illustrates characteristics of the customer's brand and the style your logo design should communicate.

```html
<!DOCTYPE html>
<html lang="en">
<head>
<meta charset="utf-8">
<title>Four nights beside the quiet harbour — book cover</title>
<link rel="stylesheet" href="https://fonts.googleapis.com/css2?family=Abril+Fatface&family=Great+Vibes&family=Open+Sans:wght@400;600&display=swap">
<style>
  :root {
    --ink: #000000;
    --paper: #ffffff;
    --magenta: #e8185f;
    --rose: #f0468a;
    --plum: #5a2a86;
    --silver: #c9c4cc;
    --display: "Abril Fatface", "Bodoni Moda", serif;
    --script: "Great Vibes", cursive;
    --body: "Open Sans", Arial, sans-serif;
  }
  * { margin: 0; padding: 0; box-sizing: border-box; }
  html, body { width: 1200px; height: 796px; overflow: hidden; background: var(--ink); }
  .cover-spread { position: relative; width: 1200px; height: 796px; background: var(--ink); }

  .back-cover { position: absolute; left: 0; top: 0; width: 669px; height: 796px; }
  .back-title { position: absolute; left: 0; top: 0; }
  .blurb {
    position: absolute; left: 60px; top: 222px; width: 411px;
    font-family: var(--body); font-size: 13.4px; line-height: 25.8px;
    color: var(--paper); text-align: justify; text-align-last: center;
  }
  .blurb p + p { margin-top: 25.8px; }

  .spine { position: absolute; left: 0; top: 0; }

  .front-cover { position: absolute; left: 669px; top: 0; width: 531px; height: 796px; overflow: hidden; }
  .cover-photo {
    position: absolute; inset: 0;
    background:
      radial-gradient(ellipse 45% 60% at 95% 45%, rgba(201,196,204,0.9), rgba(201,196,204,0) 70%),
      radial-gradient(ellipse 40% 30% at 85% 10%, rgba(240,160,200,0.8), rgba(240,160,200,0) 70%),
      linear-gradient(150deg, var(--plum) 0%, var(--magenta) 30%, var(--rose) 60%, var(--magenta) 85%, #b8125a 100%);
  }
  .front-type { position: absolute; left: 0; top: 0; }
  .publisher {
    position: absolute; left: 0; width: 531px; top: 757px;
    text-align: center; font-family: var(--body); font-weight: 600;
    font-size: 12.2px; letter-spacing: 1px; color: var(--paper);
    padding-left: 36px;
  }
  text.display { font-family: var(--display); fill: var(--paper); }
  text.script { font-family: var(--script); fill: var(--paper); }
</style>
</head>
<body>
<main class="cover-spread">

  <section class="back-cover">
    <svg class="back-title" width="669" height="220" viewBox="0 0 669 220">
      <text class="display" x="63" y="186" font-size="66" textLength="150" lengthAdjust="spacingAndGlyphs">FOUR NIGHTS</text>
      <text class="script" x="220" y="186" font-size="32" textLength="138" lengthAdjust="spacingAndGlyphs">beside the quiet</text>
      <text class="display" x="362" y="186" font-size="66" textLength="111" lengthAdjust="spacingAndGlyphs">HARBOUR</text>
    </svg>
    <div class="blurb">
      <p>A senior lady (70 years old), divorced, with a beautiful face, still wants to seduce, even young men.We found the perfect photo for the woman. We would like to ask you to make a modern cover from it.A senior lady (70 years old), divorced, with a beautiful face, still wants to seduce, even young men.</p>
      <p>We found the perfect photo for the woman. We would like to ask you to make a modern cover from it.A senior lady (70 years old), divorced, with a beautiful face, still wants to seduce, even young men. We found the perfect photo for the woman. We would like to ask you to make a modern cover from it.A senior lady (70 years old), divorced, with a beautiful face, still wants to seduce, even young men.</p>
      <p>We found the perfect photo for the woman. We would like to ask you to make a modern cover from it.</p>
    </div>
  </section>

  <svg class="spine" width="669" height="796" viewBox="0 0 669 796">
    <g transform="translate(574,52) rotate(90)">
      <text class="display" x="0" y="0" font-size="76" textLength="172" lengthAdjust="spacingAndGlyphs">FOUR NIGHTS</text>
      <text class="script" x="180" y="-2" font-size="40" textLength="152" lengthAdjust="spacingAndGlyphs">beside the quiet</text>
      <text class="display" x="338" y="0" font-size="76" textLength="125" lengthAdjust="spacingAndGlyphs">HARBOUR</text>
    </g>
    <g transform="translate(586,572) rotate(90)">
      <text class="script" x="0" y="0" font-size="48" textLength="190" lengthAdjust="spacingAndGlyphs">Mireille Cantal</text>
    </g>
  </svg>

  <section class="front-cover">
    <div class="cover-photo" role="img" aria-label="Close-up photograph of a 70-year-old woman's lower face half hidden behind windswept pink and silver hair"></div>
    <svg class="front-type" width="531" height="796" viewBox="0 0 531 796">
      <text class="display" x="55" y="198" font-size="214" textLength="214" lengthAdjust="spacingAndGlyphs">FOUR</text>
      <text class="display" x="54" y="352" font-size="214" textLength="220" lengthAdjust="spacingAndGlyphs">NIGHTS</text>
      <text class="script" x="54" y="424" font-size="72" textLength="318" lengthAdjust="spacingAndGlyphs">beside the quiet</text>
      <text class="display" x="54" y="621" font-size="240" textLength="413" lengthAdjust="spacingAndGlyphs">HARBOUR</text>
      <text class="script" x="53" y="718" font-size="100" textLength="430" lengthAdjust="spacingAndGlyphs">Mireille Cantal</text>
    </svg>
    <div class="publisher">PUBLISHER : EDITIONS BASALTE</div>
  </section>

</main>
</body>
</html>
```